Local Electrical company need some kick ass business cards

In need of some in your face design business cards for a family owned electrical service company in Edmonton, Alberta Canada. We provide reliable and trustworthy electrical service for commercial and residential work in the Edmonton and area. We have been in business for 25 years.

Target Market(s)

Residential and commercial electrical

Industry/Entity Type

Business

Contact Information for Business Card

Your welcome to change and modify the Vantor Wiring logo. please include the lightbulb! Our Colours are black and green please stay with that.
Please include a name phone number and address on the card
phone number - 780-555-0138
#22, 418 Maple Ridge Rd, St.Albert, Alberta.
Two things that need to be on the card.
"your friendly neighborhood electrictrician"
Commercial & residential electrical repair and service

Colors
9bcb3c

Requirements
Must have
• Light bulb guy Attached
• "your friendly neighborhood electrictrician"
• Commercial & residential electrical repair and service
• phone number - 780-555-0138
• #22, 418 Maple Ridge Rd, St.Albert, Alberta.
• Our colours are black and green
Nice to have
• go wild i want something loud

```html
<!DOCTYPE html>
<html lang="en">
<head>
<meta charset="utf-8">
<title>Vantor Wiring – Business Cards</title>
<link rel="stylesheet" href="https://fonts.googleapis.com/css2?family=Open+Sans:wght@400;600;700;800&display=swap">
<style>
  :root {
    --bg: #e4e6e3;
    --green: #9bcb3c;
    --green-light: #a9d84a;
    --green-deep: #5fb23a;
    --black: #111111;
    --white: #ffffff;
  }
  * { box-sizing: border-box; margin: 0; padding: 0; }
  html, body { width: 1200px; height: 1000px; overflow: hidden; }
  body {
    background: var(--bg);
    font-family: "Open Sans", Arial, sans-serif;
    position: relative;
  }
  .card {
    position: absolute;
    left: 280px;
    width: 640px;
    height: 366px;
    border-radius: 4px;
    overflow: hidden;
    box-shadow: 0 10px 30px rgba(0,0,0,.25);
    background: linear-gradient(135deg, var(--green-deep) 0%, var(--green) 55%, var(--green-light) 100%);
  }
  .card--back { top: 80px; }
  .card--front { top: 540px; }

  /* Back */
  .back-brand {
    position: absolute;
    inset: 0;
    display: flex;
    align-items: center;
    justify-content: center;
    gap: 22px;
  }
  .back-brand__dot {
    width: 46px; height: 46px;
    border-radius: 50%;
    background: var(--black);
  }
  .back-brand__name {
    font-weight: 800;
    font-size: 64px;
    color: var(--black);
    letter-spacing: 1px;
  }

  /* Front */
  .front-panel {
    position: absolute;
    top: 0; right: 0;
    width: 300px; height: 366px;
  }
  .mascot {
    position: absolute;
    top: 22px; right: 40px;
    width: 190px; height: 310px;
    border-radius: 90px 90px 40px 40px;
    background: linear-gradient(180deg, #d8ecff 0%, #b9c4cc 70%, #8f979d 100%);
  }
  .front-content {
    position: absolute;
    left: 36px; top: 34px;
    width: 360px;
  }
  .front-brand {
    font-weight: 800;
    font-size: 44px;
    line-height: 1;
    color: var(--black);
  }
  .tagline {
    margin-top: 40px;
    font-size: 14px;
    font-weight: 600;
    color: var(--black);
  }
  .services {
    margin-top: 6px;
    color: var(--white);
    font-weight: 800;
    text-transform: uppercase;
    line-height: 1.15;
  }
  .services__main { font-size: 22px; }
  .services__sub { font-size: 15px; font-weight: 700; }
  .contact {
    margin-top: 34px;
    list-style: none;
    color: var(--black);
    font-size: 16px;
    font-weight: 600;
  }
  .contact li {
    display: flex;
    align-items: flex-start;
    gap: 10px;
    margin-bottom: 4px;
    line-height: 1.2;
  }
  .contact svg { flex: none; margin-top: 2px; }
</style>
</head>
<body>

  <section class="card card--back" aria-label="Business card back">
    <div class="back-brand">
      <span class="back-brand__dot"></span>
      <span class="back-brand__name">Vantor Wiring</span>
    </div>
  </section>

  <section class="card card--front" aria-label="Business card front">
    <svg class="front-panel" viewBox="0 0 300 366" preserveAspectRatio="none" aria-hidden="true">
      <path d="M300 0 H40 C10 60 10 120 40 170 C70 230 60 300 30 366 H300 Z" fill="var(--black)"/>
    </svg>
    <div class="mascot" role="img" aria-label="Cartoon light bulb mascot wearing a green cap, arms open in welcome"></div>

    <div class="front-content">
      <div class="front-brand">Vantor Wiring</div>
      <p class="tagline">"your friendly neighborhood electrictrician"</p>
      <div class="services">
        <div class="services__main">Commercial &amp; Residential</div>
        <div class="services__sub">Electrical Repair and Service</div>
      </div>
      <ul class="contact">
        <li>
          <svg width="16" height="16" viewBox="0 0 24 24" aria-hidden="true"><path fill="var(--white)" d="M6.6 10.8a15.1 15.1 0 0 0 6.6 6.6l2.2-2.2a1 1 0 0 1 1-.25 11.4 11.4 0 0 0 3.6.57 1 1 0 0 1 1 1V20a1 1 0 0 1-1 1A17 17 0 0 1 3 4a1 1 0 0 1 1-1h3.5a1 1 0 0 1 1 1c0 1.25.2 2.45.57 3.57a1 1 0 0 1-.25 1z"/></svg>
          <span>780-555-0138</span>
        </li>
        <li>
          <svg width="16" height="18" viewBox="0 0 24 24" aria-hidden="true"><path fill="var(--white)" d="M12 2a7 7 0 0 0-7 7c0 5.25 7 13 7 13s7-7.75 7-13a7 7 0 0 0-7-7zm0 9.5A2.5 2.5 0 1 1 12 6.5a2.5 2.5 0 0 1 0 5z"/></svg>
          <span>#22, 418 Maple Ridge Rd, St.Albert<br>Alberta</span>
        </li>
      </ul>
    </div>
  </section>

</body>
</html>
```